Digital marketing agency needs a new website design

We need a new responsive design for our website: https://brovexa.com/

Brovexa is a french digital marketing company who specializes in helping companies rank higher on Quorvel search engine for their keywords in order to be more visible and have more traffic and clients.

I need you to design these 5 pages:
- Home page: https://brovexa.com
- Pricing page: https://brovexa.com/packs-backlinks/
- Contact page: https://brovexa.com/contact/
- Thank you page: https://brovexa.com/merci-temp/
- Simple page : https://brovexa.com/a-propos/

Here is a list of websites that we like their design. Use it for inspiration, but make sure it is different :

https://lumaqest.io/ (this is the one I like the most)
https://vobru.com/
http://www.kelvarnet.com/
https://talumbrel.fr/
https://www.dravosket.com/home
https://tenwhistle.com/fr/
https://wakomi.io/
https://sorbanelle.fr/

I want a 75% color background and 25% white. You should use many bright/pastel colors like this website : https://lumaqest.io/

Keep the contact form in the website header.

Target Market(s)

small business owners

Industry/Entity Type

Digital Marketing

Number of Pages Required

5+ page

Font styles to use
Sans Serif

Colors

Designer to choose colors to be used in the design.

Requirements
Must have
• Contact form in header.
• Prominent call-to-action buttons.
• Use of at least 1 flashy color, possible to use many.
• Keep the 3 chart images.
• Keep client testimonials

```html
<!DOCTYPE html>
<html lang="en">
<head>
<meta charset="utf-8">
<title>Brovexa — French Backlinks On Quality Magazines And Blogs</title>
<link rel="stylesheet" href="https://fonts.googleapis.com/css2?family=Raleway:wght@400;500;600;700&family=Lato:wght@400;700&display=swap">
<style>
:root{
  --hero-a:#4f86e6;
  --hero-b:#8b5cf6;
  --pink:#f2789f;
  --pink-soft:#ef8dbd;
  --yellow:#ffc65a;
  --blue-title:#1f76c9;
  --ink:#2b2b33;
  --grey:#5d5d66;
  --results-a:#7d8cf5;
  --results-b:#7d54ee;
  --footer:#2e2e2e;
  --white:#ffffff;
  --line:#d9d9df;
  --chart:#2d8fd5;
  --chart-fill:#dcecf8;
}
*{box-sizing:border-box;margin:0;padding:0}
html,body{width:1200px;height:3689px;overflow:hidden}
body{font-family:'Lato',sans-serif;color:var(--ink);background:var(--white);position:relative}
.h{font-family:'Raleway',sans-serif}
section,footer{position:absolute;left:0;width:1200px;overflow:hidden}
.abs{position:absolute}

/* hero */
.hero{top:0;height:795px;background:linear-gradient(110deg,var(--hero-a) 0%,#6c78ee 45%,var(--hero-b) 100%)}
.hero-waves{position:absolute;left:0;top:0}
.logo{position:absolute;font-family:'Raleway',sans-serif;font-weight:600;letter-spacing:6px;color:var(--white);font-size:40px}
.hero .logo{left:120px;top:30px}
.logo-dot{display:inline-block;width:10px;height:10px;background:var(--yellow);border-radius:50%;margin-left:6px;vertical-align:middle}
.nav{position:absolute;top:46px;left:762px;display:flex;gap:26px;align-items:center;font-family:'Raleway',sans-serif;font-size:16px;color:var(--white)}
.lang{width:123px;height:36px;background:var(--yellow);border-radius:3px;display:flex;align-items:center;justify-content:space-between;padding:0 16px;margin-left:40px}
.lang-flag{width:16px;height:12px;background:#f7a233;border:1px solid #fff7}
.hero-copy{position:absolute;left:152px;top:178px;color:var(--white);font-family:'Raleway',sans-serif}
.hero-kicker{font-size:27px;font-weight:600}
.hero-title{font-size:44px;font-weight:500;line-height:60px;margin-top:16px}
.hero-target{font-size:34px;font-weight:700;margin-top:8px}
.hero-note{font-family:'Lato',sans-serif;font-size:14px;margin-top:14px}
.btn{display:flex;align-items:center;justify-content:center;background:var(--yellow);color:var(--white);font-family:'Raleway',sans-serif;font-weight:600;border-radius:3px}
.hero .btn{position:absolute;left:152px;top:448px;width:148px;height:36px;font-size:15px}
.form-card{position:absolute;left:654px;top:165px;width:374px;height:420px;background:var(--white);border-radius:4px;box-shadow:0 10px 30px #2a2a6040;padding:26px 44px}
.form-card h2{font-family:'Raleway',sans-serif;font-weight:500;font-size:31px;color:#4a4a52;margin-bottom:24px}
.field-label{font-size:12px;color:#8a8a92;margin-bottom:6px}
.field{border:1px solid #cfcfd6;border-radius:2px;height:39px;margin-bottom:20px;width:286px}
.field.area{height:94px;padding:10px 12px;font-size:11px;line-height:16px;color:#7d7d86}
.form-card .btn{width:113px;height:35px;margin:14px auto 0;font-size:14px}

/* intro */
.intro{top:795px;height:329px;text-align:center}
.intro h2{font-family:'Raleway',sans-serif;font-weight:600;color:var(--blue-title);font-size:36px;line-height:52px;margin-top:66px}
.intro p{font-size:28px;color:var(--grey);line-height:40px;margin-top:22px}

/* results */
.results{top:1124px;height:1249px;background:linear-gradient(160deg,var(--results-a) 0%,#7c6ff2 50%,var(--results-b) 100%)}
.results h2{position:absolute;top:70px;width:100%;text-align:center;color:var(--white);font-family:'Raleway',sans-serif;font-weight:500;font-size:36px}
.chart{position:absolute;width:480px;height:281px;background:var(--white);box-shadow:0 6px 18px #30206040}
.stat{position:absolute;color:var(--white);font-family:'Raleway',sans-serif}
.stat strong{display:block;font-size:40px;font-weight:600;line-height:50px}
.stat span{display:block;font-family:'Lato',sans-serif;font-size:24px;line-height:30px;margin-top:8px}

/* testimonials */
.reviews{top:2373px;height:492px;background:var(--white)}
.reviews h2{position:absolute;top:66px;width:100%;text-align:center;font-family:'Raleway',sans-serif;font-weight:500;font-size:36px;color:#33333b}
.review{position:absolute;top:135px;width:298px;height:175px;border:1px solid #f3cf96;border-radius:3px;padding:18px 24px}
.review h3{font-family:'Raleway',sans-serif;font-size:17px;font-weight:600;color:#222}
.review .role{font-size:13px;color:#3f8fd6;margin:6px 0 10px}
.review p{font-size:12px;line-height:19px;color:#666}
.avatar{position:absolute;left:24px;bottom:-42px;width:62px;height:62px;border-radius:50%;border:3px solid #f3bd6c;background:linear-gradient(135deg,#c9a37d,#7b6a5c)}
.dots{position:absolute;top:410px;left:582px;display:flex;gap:6px}
.dots i{width:9px;height:9px;border-radius:50%;background:#cfcfd6}
.dots i:first-child{background:var(--pink)}

/* request */
.request{top:2865px;height:524px;background:linear-gradient(120deg,#ee6aa4 0%,var(--pink-soft) 60%,#e68ac5 100%)}
.request h2{position:absolute;top:70px;width:100%;text-align:center;color:var(--white);font-family:'Raleway',sans-serif;font-weight:500;font-size:36px}
.request .lead{position:absolute;top:136px;left:140px;width:920px;text-align:center;color:var(--white);font-size:19px;line-height:29px}
.request .lead u{font-weight:700}
.req-label{position:absolute;font-size:12px;color:var(--white)}
.req-field{position:absolute;background:var(--white);border-radius:2px}
.request .btn{position:absolute;left:543px;top:396px;width:114px;height:37px;font-size:14px}

/* footer */
.site-footer{top:3389px;height:300px;background:var(--footer);color:var(--white)}
.site-footer .logo{left:152px;top:72px;font-size:32px;letter-spacing:5px}
.follow{position:absolute;left:138px;top:136px;font-size:17px;display:flex;align-items:center;gap:12px}
.social{width:28px;height:28px;border-radius:50%;background:var(--white)}
.divider{position:absolute;top:64px;width:1px;height:120px;background:#5a5a5a}
.foot-links{position:absolute;top:70px;list-style:none;font-size:15px;line-height:34px}
.foot-links li::before{content:"» ";color:#ccc}
.contact-block{position:absolute;left:900px;top:68px;font-size:12px;line-height:18px}
.contact-block b{display:block;font-size:17px;margin-bottom:10px}
.copyright{position:absolute;top:3655px;width:100%;text-align:center;font-size:11px;color:#555}
</style>
</head>
<body>

<section class="hero">
  <svg class="hero-waves" width="1200" height="795" viewBox="0 0 1200 795" aria-hidden="true">
    <path d="M0 510 C160 560 380 620 560 795 L0 795 Z" fill="var(--pink)"/>
    <path d="M0 515 C200 540 420 610 545 795 L520 795 C420 650 230 575 0 545 Z" fill="#fff"/>
    <path d="M560 795 C720 640 980 560 1200 560 L1200 795 Z" fill="#8a5cf3" opacity=".55"/>
    <path d="M640 0 C900 60 1050 0 1200 20 L1200 0 Z" fill="#ffffff" opacity=".12"/>
  </svg>
  <div class="logo">BROVEXA<span class="logo-dot"></span></div>
  <nav class="nav"><span>Results</span><span>References</span><span class="lang"><span class="lang-flag"></span>Eng<span>&#8964;</span></span></nav>
  <div class="hero-copy">
    <div class="hero-kicker">French Backlinks On</div>
    <div class="hero-title">Quality Magazines<br>And Blogs</div>
    <div class="hero-target">Trust Flow Target 15-20</div>
    <div class="hero-note">Only Quality Backlinks Help Increase Your Traffic On Quorvel</div>
  </div>
  <a class="btn">See The Results</a>
  <form class="form-card">
    <h2>Information &amp; Rates</h2>
    <div class="field-label">Your email</div><div class="field"></div>
    <div class="field-label">Website</div><div class="field"></div>
    <div class="field-label">How can we help you ?</div>
    <div class="field area">J'aimerais obtenir des backlinks pour améliorer les positions de notre site sur Quorvel pour nos mots-clés et générer plus de trafic.</div>
    <div class="btn">To Send</div>
  </form>
</section>

<section class="intro">
  <h2>Get Backlinks On Quality Sites That Have A High<br>Trust Flow And Increase Your Traffic On Quorvel.</h2>
  <p>We support most themes and write articles. No return link<br>needed. Without engagement.</p>
</section>

<section class="results">
  <svg class="abs" style="left:0;top:0" width="1200" height="1249" aria-hidden="true">
    <path d="M720 0 C640 300 900 420 760 700 C650 920 820 1100 760 1249 L1200 1249 L1200 0 Z" fill="#8a5df2" opacity=".35"/>
  </svg>
  <h2>Examples Of Results Obtained With Our Backlinks</h2>

  <svg class="chart" style="left:120px;top:179px" viewBox="0 0 480 281" role="img" aria-label="Line chart of monthly sessions rising to 26 000">
    <rect width="480" height="28" fill="#595959"/><circle cx="16" cy="14" r="4" fill="#fff"/><circle cx="28" cy="14" r="4" fill="#fff"/><circle cx="40" cy="14" r="4" fill="#fff"/>
    <text x="10" y="46" font-size="9" font-family="Lato" font-weight="700">Explorer</text>
    <text x="10" y="62" font-size="8" font-family="Lato">Summary</text><text x="56" y="62" font-size="8" fill="#2d6fc4" font-family="Lato">Site Usage  Ecommerce  AdPanel</text>
    <line x1="10" y1="66" x2="470" y2="66" stroke="#ddd"/>
    <text x="390" y="84" font-size="7" font-family="Lato">Day  Week  Month</text>
    <circle cx="14" cy="100" r="3" fill="var(--chart)"/><text x="22" y="103" font-size="8" font-family="Lato">Sessions</text>
    <polygon points="10,248 60,248 100,244 130,236 160,208 190,188 220,198 260,202 300,206 340,210 380,204 420,200 450,180 470,158 470,248" fill="var(--chart-fill)"/>
    <polyline points="10,248 60,248 100,244 130,236 160,208 190,188 220,198 260,202 300,206 340,210 380,204 420,200 450,180 470,158" fill="none" stroke="var(--chart)" stroke-width="2"/>
    <text x="20" y="266" font-size="7" font-family="Lato">April 2017     July 2017     October 2017     January 2018     April 2018     July 2018</text>
  </svg>
  <div class="stat" style="left:659px;top:246px"><strong>From 0 to 26 000<br>visits / month</strong><span>And it continues to increase!</span></div>

  <svg class="chart" style="left:600px;top:538px" viewBox="0 0 480 281" role="img" aria-label="Line chart of monthly sessions rising from 1,200 to 4,400">
    <rect width="480" height="28" fill="#595959"/><circle cx="16" cy="14" r="4" fill="#fff"/><circle cx="28" cy="14" r="4" fill="#fff"/><circle cx="40" cy="14" r="4" fill="#fff"/>
    <text x="10" y="46" font-size="9" font-family="Lato" font-weight="700">Explorer</text>
    <text x="10" y="62" font-size="8" font-family="Lato">Summary</text><text x="56" y="62" font-size="8" fill="#2d6fc4" font-family="Lato">Site Usage  Goal Set 1  Goal Set 2  Goal Set 3  Ecommerce</text>
    <line x1="10" y1="66" x2="470" y2="66" stroke="#ddd"/>
    <text x="390" y="84" font-size="7" font-family="Lato">Day  Week  Month</text>
    <circle cx="14" cy="100" r="3" fill="var(--chart)"/><text x="22" y="103" font-size="8" font-family="Lato">Sessions</text>
    <polygon points="10,220 60,220 100,214 130,210 160,190 200,186 240,186 280,182 320,160 350,178 390,170 420,174 460,166 470,166 470,248 10,248" fill="var(--chart-fill)"/>
    <polyline points="10,220 60,220 100,214 130,210 160,190 200,186 240,186 280,182 320,160 350,178 390,170 420,174 460,166" fill="none" stroke="var(--chart)" stroke-width="2"/>
    <g fill="var(--chart)"><circle cx="100" cy="214" r="3"/><circle cx="160" cy="190" r="3"/><circle cx="240" cy="186" r="3"/><circle cx="320" cy="160" r="3"/><circle cx="390" cy="170" r="3"/><circle cx="460" cy="166" r="3"/></g>
    <text x="60" y="266" font-size="7" font-family="Lato">July 2017          October 2017          January 2018          April 2018</text>
  </svg>
  <div class="stat" style="left:157px;top:606px"><strong>From 1,200 to 4,400<br>visits / month</strong><span>Traffic from Quorvel has more than<br>tripled in 12 months.</span></div>

  <svg class="chart" style="left:120px;top:892px" viewBox="0 0 480 281" role="img" aria-label="Line chart of weekly sessions rising to 60 000">
    <rect width="480" height="28" fill="#595959"/><circle cx="16" cy="14" r="4" fill="#fff"/><circle cx="28" cy="14" r="4" fill="#fff"/><circle cx="40" cy="14" r="4" fill="#fff"/>
    <text x="10" y="46" font-size="9" font-family="Lato" font-weight="700">Explorer</text>
    <text x="10" y="62" font-size="8" font-family="Lato">Summary</text><text x="56" y="62" font-size="8" fill="#2d6fc4" font-family="Lato">Site Usage  Ecommerce  AdPanel</text>
    <line x1="10" y1="66" x2="470" y2="66" stroke="#ddd"/>
    <text x="390" y="84" font-size="7" font-family="Lato">Day  Week  Month</text>
    <circle cx="14" cy="100" r="3" fill="var(--chart)"/><text x="22" y="103" font-size="8" font-family="Lato">Sessions</text>
    <polygon points="10,248 80,248 110,246 130,232 150,220 170,200 185,194 200,204 215,180 235,178 250,196 265,190 285,204 305,198 320,208 340,196 360,190 380,204 400,196 420,206 440,194 455,188 470,196 470,248" fill="var(--chart-fill)"/>
    <polyline points="10,248 80,248 110,246 130,232 150,220 170,200 185,194 200,204 215,180 235,178 250,196 265,190 285,204 305,198 320,208 340,196 360,190 380,204 400,196 420,206 440,194 455,188 470,196" fill="none" stroke="var(--chart)" stroke-width="2"/>
    <text x="30" y="266" font-size="7" font-family="Lato">July 2017       October 2017       January 2018       April 2018       July 2018</text>
  </svg>
  <div class="stat" style="left:659px;top:958px"><strong>From 0 to 60 000<br>visits / week</strong><span>This is more than 240 000<br>visits per month for this site.</span></div>
</section>

<section class="reviews">
  <h2>This Is What Our Customers Think</h2>
  <article class="review" style="left:138px">
    <h3>Marcel Thiaudière</h3><div class="role">Owner - Velvet Ribbon</div>
    <p>They drove netlinking campaigns for our online store, which resulted in more than 50 quality links and improved the overall positioning</p>
    <div class="avatar" role="img" aria-label="Customer portrait"></div>
  </article>
  <article class="review" style="left:467px">
    <h3>Lucien Farvelle</h3><div class="role">Owner - Farvelle Media</div>
    <p>In a few months, we have moved to the first page of Quorvel for all targeted keywords. The agency is very professional and works methodically...</p>
    <div class="avatar" role="img" aria-label="Customer portrait"></div>
  </article>
  <article class="review" style="left:797px">
    <h3>Remy Osterlin</h3><div class="role">Owner - Ondine Voyages</div>
    <p>They drove netlinking campaigns for our online store, which resulted in more than 50 quality links and improved the overall positioning</p>
    <div class="avatar" role="img" aria-label="Customer portrait"></div>
  </article>
  <div class="dots"><i></i><i></i><i></i></div>
</section>

<section class="request">
  <svg class="abs" style="left:0;top:0" width="1200" height="524" aria-hidden="true">
    <path d="M0 340 C200 300 420 380 520 524 L0 524 Z" fill="#f08fb8" opacity=".5"/>
    <path d="M520 524 C600 400 500 300 640 240 C800 170 1000 260 1200 200 L1200 524 Z" fill="#e478b7" opacity=".35"/>
  </svg>
  <h2>Information Request</h2>
  <p class="lead">Would you like more information or pricing? Fill in the short contact form and tell us about your SEO needs and goals. The rates of the backlinks vary according to the theme ... <u>Contact Us</u></p>
  <span class="req-label" style="left:202px;top:224px">Your email</span>
  <div class="req-field" style="left:202px;top:246px;width:373px;height:39px"></div>
  <span class="req-label" style="left:202px;top:296px">Website</span>
  <div class="req-field" style="left:202px;top:319px;width:373px;height:40px"></div>
  <span class="req-label" style="left:622px;top:224px">How can we help you ?</span>
  <div class="req-field" style="left:622px;top:243px;width:376px;height:113px;padding:12px;font-size:12px;line-height:17px;color:#555">J'aimerais obtenir des backlinks pour améliorer les positions de notre site sur Quorvel pour nos mots-clés et générer plus de trafic.</div>
  <a class="btn">To Send</a>
</section>

<footer class="site-footer">
  <svg class="abs" style="left:0;top:0" width="1200" height="300" aria-hidden="true">
    <path d="M0 145 C250 195 500 210 740 250 C900 275 1050 280 1200 275 L1200 300 L0 300 Z" fill="#ffffff"/>
    <path d="M0 150 C220 195 480 215 720 245 C500 230 250 225 0 215 Z" fill="#29b3e8"/>
    <path d="M0 180 C200 210 420 235 640 250 C420 250 200 250 0 248 Z" fill="#2a5fd8"/>
  </svg>
  <div class="logo">BROVEXA<span class="logo-dot"></span></div>
  <div class="follow">Follow US On : <span class="social"></span></div>
  <div class="divider" style="left:381px"></div>
  <ul class="foot-links" style="left:418px"><li>Home</li><li>Improve your SEO</li><li>My account</li></ul>
  <div class="divider" style="left:634px"></div>
  <ul class="foot-links" style="left:676px"><li>Legal Notice</li><li>About</li><li>Contact</li></ul>
  <div class="divider" style="left:873px"></div>
  <div class="contact-block">Call Us On :<b>(321) 555 0148</b>Call Us On :<b>info@brovexa.com</b></div>
  <div class="divider" style="left:1078px"></div>
</footer>
<div class="copyright">© 2018 Brovexa | All Rights Reserved.</div>

</body>
</html>
```